New website for Holloway Law Firm at www.keepfirmplan.example

We are a professional law firm located in the Nashville, Tennessee USA area. We focus on personal injury law. We are looking for a slick new website that is user friendly for updating with new blogs, videos, etc. The primary colors should be red, black, and white. It should load extremely fast and have a good mobile component. The pages for the design will include a home page, about us, news, contact us, and practice page. The practice page will be copied for all the practice areas including motor vehicle accidents, slip and fall accidents, dog bites, etc. We have included an image which we would like to include in the new site which shows the color scheme The image is called banner-Car Wreck. The new website should NOT have gavels, court houses, law books, scales or the typical images for a law firm.

Target Market(s)

People in Tennessee involved in accidents

Industry/Entity Type

Legal services, law firm

Number of Pages Required

5+ page

Font styles to use
Serif

Colors
EB3D1F
EC4F4E
F09395
F8D3D4
FCEDEE

Requirements
Should not have
• Gavels, columns, scales, law related images

```html
<!DOCTYPE html>
<html lang="en">
<head>
<meta charset="utf-8">
<title>Holloway Law Firm PLLC</title>
<link href="https://fonts.googleapis.com/css2?family=Open+Sans:wght@400;600;700&display=swap" rel="stylesheet">
<style>
:root{
  --red:#c8222b;
  --red-soft:#d23a40;
  --ink:#333333;
  --muted:#777777;
  --black:#0d0d0d;
  --white:#ffffff;
  --footer:#474747;
  --line:#c9c9c9;
}
*{box-sizing:border-box;margin:0;padding:0}
html,body{width:1200px;height:3630px;overflow:hidden;background:var(--white)}
body{position:relative;font-family:"Open Sans",sans-serif;color:var(--ink)}
.abs{position:absolute}
a{color:inherit;text-decoration:none}

/* header */
.site-header{left:0;top:0;width:1200px;height:122px}
.brand{left:125px;top:42px;width:210px;text-align:center;color:var(--red);font-weight:400;line-height:1}
.brand .name{font-size:31px;letter-spacing:1px}
.brand .sub{font-size:15px;letter-spacing:2px;margin-top:3px;display:flex;align-items:center;gap:8px;justify-content:center}
.brand .sub::before,.brand .sub::after{content:"";flex:1;height:1px;background:var(--red)}
.main-nav{left:540px;top:60px;display:flex;gap:29px;font-size:11px;color:var(--muted)}
.main-nav .active{color:var(--red);font-weight:600;border-bottom:1px solid var(--red);padding-bottom:4px}
.header-tools{left:920px;top:57px;display:flex;align-items:center;gap:14px;font-size:14px;color:#555}
.header-tools .divider{width:1px;height:20px;background:var(--line)}

/* hero */
.hero{left:0;top:122px;width:1200px;height:552px;background:var(--black)}
.hero-photo{right:0;top:0;width:760px;height:552px;background:radial-gradient(ellipse at 60% 55%,#c2222b 0%,#8a1218 35%,#2a0507 68%,#0d0d0d 100%)}
.hero-kicker{left:125px;top:192px;color:var(--white);font-size:14px}
.hero-title{left:125px;top:218px;color:var(--white);font-size:32px;font-weight:400;line-height:43px;letter-spacing:.5px}
.hero-title b{font-weight:700}
.slider-dots{left:128px;top:463px;display:flex;gap:8px}
.slider-dots span{width:22px;height:22px;border-radius:50%;background:#555;display:flex;align-items:center;justify-content:center}
.slider-dots span:first-child{background:var(--red)}

/* buttons */
.btn{height:38px;width:160px;border-radius:19px;background:var(--red);color:var(--white);font-size:11px;display:flex;align-items:center;padding-left:44px}
.btn .go{position:absolute;right:8px;top:9px;width:20px;height:20px;border-radius:50%;background:var(--black);display:flex;align-items:center;justify-content:center}
.btn.dark{background:var(--black)}
.btn.dark .go{background:var(--red)}

/* section titles */
.section-title{left:0;width:1200px;text-align:center;font-size:29px;font-weight:400;letter-spacing:1px;color:#333}

/* about */
.about-sub{left:0;top:818px;width:1200px;text-align:center;font-size:11px;color:#999}
.about-text{left:275px;top:852px;width:650px;text-align:center;font-size:11px;line-height:22px;color:#666}

/* practice */
.practice-band{left:0;top:1300px;width:1200px;height:632px}
.card{width:300px;height:404px;background:var(--white);border-radius:6px;box-shadow:0 2px 10px rgba(0,0,0,.12);overflow:hidden;text-align:center;top:1153px}
.card .photo{height:219px}
.card h3{font-size:15px;font-weight:600;color:#444;line-height:20px;margin-top:20px;letter-spacing:.5px}
.card .rule{width:40px;height:1px;background:var(--red);margin:10px auto 12px}
.card p{font-size:11px;line-height:16px;color:#555;padding:0 28px}
.card .more{width:20px;height:20px;border-radius:50%;background:var(--red);margin:12px auto 0;display:flex;align-items:center;justify-content:center}
.quote{left:150px;top:1698px;width:900px;text-align:center;color:var(--white);font-size:25px;line-height:34px;letter-spacing:.5px}
.quote-source{left:0;top:1841px;width:1200px;text-align:center;color:var(--white);font-size:11px}

/* news */
.news-item{overflow:hidden}
.news-item .photo{position:absolute;inset:0}
.news-caption{position:absolute;left:14px;bottom:14px;color:var(--white);font-size:12px;line-height:17px;letter-spacing:.3px}
.news-meta{display:flex;gap:18px;font-size:11px;margin-top:3px;align-items:center}
.news-meta span{display:flex;gap:6px;align-items:center}
.play{position:absolute;border:2px solid rgba(255,255,255,.85);border-radius:50%;display:flex;align-items:center;justify-content:center}
.news-item.large .news-caption{left:41px;bottom:40px;font-size:20px;line-height:28px}

/* contact */
.contact-photo{left:125px;top:2704px;width:455px;height:340px}
.contact-title{left:618px;top:2695px;font-size:30px;font-weight:400;letter-spacing:1px;color:#333}
.contact-sub{left:621px;top:2740px;font-size:11px;color:#666}
.field{border:1px solid #aaa;font-size:11px;color:#555;padding:12px 11px;background:var(--white)}

/* footer */
.site-footer{left:0;top:3195px;width:1200px;height:360px;background:var(--footer);color:var(--white)}
.foot-brand{left:125px;top:3283px;width:207px;text-align:center;color:var(--white);line-height:1}
.foot-brand .name{font-size:31px;letter-spacing:1px}
.foot-brand .sub{font-size:15px;letter-spacing:2px;margin-top:3px;display:flex;align-items:center;gap:8px}
.foot-brand .sub::before,.foot-brand .sub::after{content:"";flex:1;height:1px;background:var(--white)}
.foot-info{color:var(--white);font-size:11px;line-height:18px;display:flex;gap:10px;align-items:flex-start}
.foot-head{color:var(--white);font-size:12px;letter-spacing:.5px}
.foot-head::after{content:"";display:block;width:36px;height:1px;background:var(--white);margin-top:7px}
.foot-links{list-style:none;font-size:11px;color:var(--white)}
.foot-links li{height:30.5px;display:flex;gap:9px;align-items:center}
.news-input{left:632px;top:3380px;width:179px;height:36px;border-radius:18px;background:var(--white);color:#555;font-size:9px;padding:12px 18px}
.subscribe{left:632px;top:3430px;width:179px;height:36px;border-radius:18px;background:var(--red);color:var(--white);font-size:9px;text-align:center;line-height:36px}
.map{left:876px;top:3330px;width:198px;height:136px;border:4px solid var(--white);background:linear-gradient(135deg,#e9ece4,#d8e0d2 55%,#c9d6e4)}
.copyright{left:125px;top:3580px;font-size:11px;color:#444}
.copyright em{font-style:normal;color:var(--red)}
.socials{left:934px;top:3575px;display:flex;gap:9px}
.socials span{width:28px;height:28px;border-radius:50%;background:#333}
.socials span:first-child{background:var(--red)}
</style>
</head>
<body>

<header class="site-header abs">
  <div class="brand abs"><div class="name">HOLLOWAY</div><div class="sub">LAW FIRM PLLC</div></div>
  <nav class="main-nav abs">
    <a class="active">Home</a><a>About us</a><a>Practice Areas</a><a>News</a><a>Contact us</a>
  </nav>
  <div class="header-tools abs">
    <svg width="15" height="15" viewBox="0 0 15 15"><circle cx="6" cy="6" r="4.8" fill="none" stroke="#777" stroke-width="1.3"/><line x1="9.5" y1="9.5" x2="14" y2="14" stroke="#777" stroke-width="1.3"/></svg>
    <span class="divider"></span>
    <span>(615) 555-0142</span>
  </div>
</header>

<section class="hero abs">
  <div class="hero-photo abs" role="img" aria-label="Red car shattering its windscreen in a collision"></div>
  <div class="hero-kicker abs">HOLLOWAY LAW FIRM PLLC</div>
  <h1 class="hero-title abs">DON’T LOSE WHAT’S<br><b>LEGALLY</b> YOURS</h1>
  <div class="slider-dots abs">
    <span><svg width="8" height="8" viewBox="0 0 8 8"><path d="M5 1 2 4l3 3" fill="none" stroke="#fff" stroke-width="1.4"/></svg></span>
    <span><svg width="8" height="8" viewBox="0 0 8 8"><path d="M3 1l3 3-3 3" fill="none" stroke="#fff" stroke-width="1.4"/></svg></span>
  </div>
</section>

<h2 class="section-title abs" style="top:770px">About us</h2>
<div class="about-sub abs">Trial Lawyers...</div>
<p class="about-text abs">WE ARE TRIAL LAWYERS AND WE ARE PROUD OF IT! &nbsp;There are many law firms in Tennessee who claim to be trial lawyers, but their attorneys have never seen a courtroom. &nbsp;We have tried hundreds of cases to verdict and we have helped thousands of people in the Tennessee courts. &nbsp;We fight against billion dollar insurance companies, billion dollar corporations, and the State of Tennessee...and we win!</p>
<a class="btn abs" style="left:520px;top:969px">Read More<span class="go"><svg width="8" height="8" viewBox="0 0 8 8"><path d="M3 1l3 3-3 3" fill="none" stroke="#fff" stroke-width="1.4"/></svg></span></a>

<svg class="practice-band abs" viewBox="0 0 1200 632" preserveAspectRatio="none" role="img" aria-label="Red band with faint photo texture"><polygon points="0,110 1200,5 1200,632 0,632" fill="var(--red)"/></svg>
<h2 class="section-title abs" style="top:1081px">Practice Areas</h2>

<article class="card abs" style="left:125px">
  <div class="photo" role="img" aria-label="Two cars damaged in a road collision" style="background:linear-gradient(180deg,#c9ccd2,#5a6272 60%,#2b3140)"></div>
  <h3>Motor Vehicle<br>Accidents</h3><div class="rule"></div>
  <p>Lorem Ipsum is simply dummy text of the printing and typesetting industry has been text ever since the 1500s,</p>
  <div class="more"><svg width="8" height="8" viewBox="0 0 8 8"><path d="M3 1l3 3-3 3" fill="none" stroke="#fff" stroke-width="1.4"/></svg></div>
</article>
<article class="card abs" style="left:450px">
  <div class="photo" role="img" aria-label="Dog biting a person's arm" style="background:linear-gradient(135deg,#6d4a2b,#b98a55 50%,#8a8f96)"></div>
  <h3 style="margin-top:27px">Dog Bites</h3><div class="rule" style="margin-bottom:19px"></div>
  <p>Lorem Ipsum is simply dummy text of the printing and typesetting industry has been text ever since the 1500s,</p>
  <div class="more"><svg width="8" height="8" viewBox="0 0 8 8"><path d="M3 1l3 3-3 3" fill="none" stroke="#fff" stroke-width="1.4"/></svg></div>
</article>
<article class="card abs" style="left:775px">
  <div class="photo" role="img" aria-label="Worker slipping on a wet floor beside a caution sign" style="background:linear-gradient(135deg,#d9d9d6,#bdbdb8 60%,#9a9a95)"></div>
  <h3>Slip And Fall<br>Accidents</h3><div class="rule"></div>
  <p>Lorem Ipsum is simply dummy text of the printing and typesetting industry has been text ever since the 1500s,</p>
  <div class="more"><svg width="8" height="8" viewBox="0 0 8 8"><path d="M3 1l3 3-3 3" fill="none" stroke="#fff" stroke-width="1.4"/></svg></div>
</article>

<a class="btn dark abs" style="left:520px;top:1598px">View More<span class="go"><svg width="8" height="8" viewBox="0 0 8 8"><path d="M3 1l3 3-3 3" fill="none" stroke="#fff" stroke-width="1.4"/></svg></span></a>
<blockquote class="quote abs">“Speak up for those who cannot speak for themselves, for the rights of all who are destitute. Speak up and judge fairly; defend the rights of the poor and needy.”</blockquote>
<div class="quote-source abs">— PROVERBS 31:8-9</div>

<h2 class="section-title abs" style="top:2014px">Latest News</h2>

<article class="news-item abs" style="left:125px;top:2101px;width:365px;height:202px">
  <div class="photo" role="img" aria-label="Dog approaching a person's legs on a street" style="background:linear-gradient(135deg,#8f949a,#5d636b 60%,#2f3338)"></div>
  <span class="play" style="right:16px;top:14px;width:28px;height:28px"><svg width="10" height="10" viewBox="0 0 10 10"><path d="M2 1l7 4-7 4z" fill="#fff"/></svg></span>
  <div class="news-caption">If a Dog Bites You, Do These<br>6 Things Now
    <div class="news-meta"><span>▢ November 27, 2021</span><span>◉ 200</span><span>▭ 05</span></div></div>
</article>
<article class="news-item abs" style="left:125px;top:2328px;width:365px;height:202px">
  <div class="photo" role="img" aria-label="Person lying on a floor after a fall" style="background:linear-gradient(135deg,#7a5a3c,#4d3a2a 55%,#24201c)"></div>
  <span class="play" style="right:16px;top:10px;width:28px;height:28px"><svg width="10" height="10" viewBox="0 0 10 10"><path d="M2 1l7 4-7 4z" fill="#fff"/></svg></span>
  <div class="news-caption">The Common Causes of Slip and Fall<br>Accidents?
    <div class="news-meta"><span>▢ November 27, 2021</span><span>◉ 200</span><span>▭ 05</span></div></div>
</article>
<article class="news-item large abs" style="left:508px;top:2101px;width:566px;height:429px">
  <div class="photo" role="img" aria-label="Distressed driver crouching near a crashed car on a road" style="background:radial-gradient(ellipse at 45% 60%,#9a3b3b 0%,#6e6e6e 30%,#8d9193 70%,#a4a8aa)"></div>
  <span class="play" style="left:250px;top:180px;width:54px;height:54px;border-width:3px"><svg width="18" height="18" viewBox="0 0 10 10"><path d="M2 1l7 4-7 4z" fill="#fff"/></svg></span>
  <div class="news-caption">What are the Most Common Types of<br>Accidents?
    <div class="news-meta" style="font-size:11px"><span>▢ November 27, 2021</span><span>◉ 200</span><span>▭ 05</span></div></div>
</article>

<a class="btn abs" style="left:520px;top:2584px">View More<span class="go"><svg width="8" height="8" viewBox="0 0 8 8"><path d="M3 1l3 3-3 3" fill="none" stroke="#fff" stroke-width="1.4"/></svg></span></a>

<div class="contact-photo abs" role="img" aria-label="Red warning triangle on a road behind a stopped car at dusk" style="background:linear-gradient(180deg,#5d7591,#3e5874 45%,#6e5a4a 75%,#4a3a30)"></div>
<h2 class="contact-title abs">Quick Contact</h2>
<div class="contact-sub abs">How Can We Help?</div>
<form>
  <div class="field abs" style="left:621px;top:2773px;width:221px;height:40px">First Name*</div>
  <div class="field abs" style="left:853px;top:2773px;width:221px;height:40px">Last Name*</div>
  <div class="field abs" style="left:621px;top:2829px;width:221px;height:40px">Phone*</div>
  <div class="field abs" style="left:853px;top:2829px;width:221px;height:40px">E-Mail*</div>
  <div class="field abs" style="left:621px;top:2885px;width:453px;height:96px">Message</div>
  <a class="btn abs" style="left:622px;top:3003px;padding-left:54px">Send<span class="go"><svg width="8" height="8" viewBox="0 0 8 8"><path d="M3 1l3 3-3 3" fill="none" stroke="#fff" stroke-width="1.4"/></svg></span></a>
</form>

<footer class="site-footer abs"></footer>
<div class="foot-brand abs"><div class="name">HOLLOWAY</div><div class="sub">LAW FIRM PLLC</div></div>
<div class="foot-info abs" style="left:125px;top:3360px">
  <svg width="14" height="16" viewBox="0 0 14 16"><path d="M7 0a5.5 5.5 0 0 0-5.5 5.5C1.5 10 7 16 7 16s5.5-6 5.5-10.5A5.5 5.5 0 0 0 7 0z" fill="#fff"/><circle cx="7" cy="5.5" r="2" fill="#474747"/></svg>
  <span>1180 Linden Park Way | Suite 210 |<br>Franklin, TN 37064</span>
</div>
<div class="foot-info abs" style="left:125px;top:3420px">
  <svg width="14" height="14" viewBox="0 0 14 14"><path d="M3 1l2.5 3-1.5 1.5c1 2 2.5 3.5 4.5 4.5L10 8.5l3 2.5-1.5 2C6 13 1 8 1 2.5z" fill="#fff"/></svg><span>(615) 555-0142</span>
</div>
<div class="foot-info abs" style="left:125px;top:3441px">
  <svg width="14" height="12" viewBox="0 0 14 12"><rect x="0" y="1" width="14" height="10" fill="#fff"/><path d="M0 1l7 5 7-5" fill="none" stroke="#474747" stroke-width="1.2"/></svg><span>office@hollowaylawfirm.example</span>
</div>

<div class="foot-head abs" style="left:443px;top:3283px">Quick Link</div>
<ul class="foot-links abs" style="left:443px;top:3313px">
  <li>›<span>Home</span></li><li>›<span>About us</span></li><li>›<span>Practice Areas</span></li><li>›<span>News</span></li><li>›<span>Contact us</span></li>
</ul>

<div class="foot-head abs" style="left:635px;top:3283px">Newsletter</div>
<p class="abs" style="left:635px;top:3320px;color:#fff;font-size:11px;line-height:16px">Join Our Newsletter To Receive<br>The Latest Update.</p>
<div class="news-input abs">Your Email</div>
<div class="subscribe abs">SUBSCRIBE</div>

<div class="foot-head abs" style="left:876px;top:3283px">Map</div>
<div class="map abs" role="img" aria-label="Map showing the office location in Tennessee"><svg class="abs" style="left:86px;top:46px" width="12" height="14" viewBox="0 0 14 16"><path d="M7 0a5.5 5.5 0 0 0-5.5 5.5C1.5 10 7 16 7 16s5.5-6 5.5-10.5A5.5 5.5 0 0 0 7 0z" fill="var(--red)"/></svg></div>

<div class="copyright abs">Copyright © 2021 <em>HOLLOWAY LAW FIRM PLLC</em>, All Rights Reserved.</div>
<div class="socials abs"><span></span><span></span><span></span><span></span></div>

</body>
</html>
```